Leadership and Team Coaching Blog Template for my company, Fenwick Marlow Pty Ltd

I need a consistent design I can use for publications. I am a leadership coach as well as a team coach and I also am a pretty good facilitator. I am to help people be their best both as individuals and as teams so as I enter semi-retirement I've been writing short articles to support my business. The final design should be flexible and elegant so you can tell the difference between different articles. It should also communicate confidence, energy and expertise and invite you to read further. I love blue and have attached my current logo. Not wedded to using it but clients recognise it and am sure someone clever can do something interesting with it

Target Market(s)

middle and senior leaders and Board members

Industry/Entity Type

It Company

Font styles to use
Sans Serif

Colors
0392cd
3176b5
3276b5
886aae
33b8a4
00a990
a54499
c588bc
876aae

Requirements
Must have
• flexibility to be able to re-use for different publications
Nice to have
• eye catching images
• elegant line drawing
Should not have
• clip art

```html
<!DOCTYPE html>
<html lang="en">
<head>
<meta charset="utf-8">
<title>Fenwick Marlow Pty Ltd — Blog</title>
<link href="https://fonts.googleapis.com/css2?family=Lustria&family=Open+Sans:wght@400;600&display=swap" rel="stylesheet">
<style>
:root{
  --blue:#3176b5;
  --navy:#2f5597;
  --teal:#1a9e8f;
  --rule:#1b8fae;
  --purple:#876aae;
  --magenta:#a54499;
  --pink:#c588bc;
  --text:#8a8a8a;
  --line:#e3e3e3;
  --footer:#2b2b2b;
  --serif:'Lustria', Georgia, serif;
  --sans:'Open Sans', Arial, sans-serif;
}
*{box-sizing:border-box;margin:0;padding:0}
html,body{width:821px;height:1200px;overflow:hidden;background:#fff}
body{position:relative;font-family:var(--sans);color:var(--text)}
a{text-decoration:none;color:inherit}

.brand{position:absolute;left:92px;top:22px;font-family:var(--serif);color:var(--navy);font-size:21px;line-height:24px;letter-spacing:.5px}
.brand small{display:block;font-size:10px;color:var(--text);letter-spacing:1.5px;margin-top:4px}

.social{position:absolute;left:459px;top:28px;display:flex;gap:4px}
.social span{width:18px;height:18px;border-radius:50%;background:#666}

.search{position:absolute;left:578px;top:22px;width:152px;height:29px;border:1px solid #d6d6d6;border-radius:2px;font-family:var(--serif);font-size:9px;color:#999;padding:9px 10px}
.search svg{position:absolute;right:9px;top:8px}

.nav{position:absolute;right:91px;top:74px;display:flex;gap:21px;font-family:var(--serif);font-size:9px;color:#666}
.nav .active{color:var(--magenta)}

.rule{position:absolute;left:0;top:100px;width:821px;height:3px;background:var(--rule)}

.hero{position:absolute;left:90px;top:114px;width:465px;height:229px;background:linear-gradient(135deg,#cbc6c0,#8f8780 55%,#5a5550)}
.hero .arrow{position:absolute;right:0;top:104px;width:17px;height:22px;background:rgba(80,80,80,.55)}
.hero .caption{position:absolute;left:0;bottom:0;width:100%;height:38px;background:rgba(135,106,174,.85);color:#fff;padding:6px 12px}
.hero h2{font-family:var(--serif);font-weight:400;font-size:10px}
.hero p{font-size:6.5px;margin-top:2px}
.btn-light{position:absolute;right:11px;top:8px;background:#fff;color:var(--magenta);font-family:var(--serif);font-size:8px;padding:5px 11px}

.posts{position:absolute;left:90px;top:359px;width:465px;display:grid;grid-template-columns:225px 225px;column-gap:15px;row-gap:0}
.post{height:241px}
.post .pic{height:136px}
.post h3{font-family:var(--serif);font-weight:400;color:var(--teal);font-size:10px;line-height:13px;margin-top:10px}
.post time{display:block;font-family:var(--serif);color:var(--purple);font-size:7px;margin-top:6px}
.post p{font-size:6.6px;line-height:11px;margin-top:7px}

.pager{position:absolute;left:90px;top:1081px;display:flex;gap:6px}
.pager span{width:16px;height:16px;border:1px solid #ccc;font-size:7px;color:var(--blue);display:flex;align-items:center;justify-content:center;font-family:var(--serif)}

.side{position:absolute;left:566px;width:164px}
.side h4{font-family:var(--serif);font-weight:400;font-size:13.5px;letter-spacing:.2px}
.latest h4{color:var(--teal)}
.popular h4,.signup h4{color:var(--magenta)}
.item{display:flex;gap:8px;height:67px;border-bottom:1px solid var(--line);padding-top:0}
.item .thumb{width:60px;height:44px;flex:none}
.item a{font-family:var(--serif);color:var(--blue);font-size:7.3px;line-height:11px;display:block}
.item .more{font-family:var(--serif);color:#999;font-size:6.5px;margin-top:6px}
.list{margin-top:7px}
.view-all{display:inline-block;margin-top:12px;border:1px solid #ddd;font-family:var(--serif);font-size:7px;color:#999;padding:8px 9px}

.promo{position:absolute;left:565px;top:445px;width:164px;height:163px;background:linear-gradient(180deg,#6a9ed4,#b9cfe4 60%,#2e2e2e)}
.promo h5{position:absolute;left:11px;top:12px;color:#fff;font-family:var(--sans);font-weight:600;font-size:17px;line-height:21px}
.promo .btn-light{left:11px;right:auto;top:60px;color:var(--blue)}

.signup form{display:flex;margin-top:6px;width:164px;height:28px;border:1px solid #ddd}
.signup .field{flex:1;font-family:var(--serif);font-size:8px;color:#999;padding:9px 11px}
.signup .send{width:19px;background:var(--pink);display:flex;align-items:center;justify-content:center}

.footer{position:absolute;left:0;top:1134px;width:821px;height:66px;background:var(--footer);color:#ccc;font-size:6.8px}
.footer nav{position:absolute;left:90px;top:20px;display:flex;gap:7px}
.footer nav i{font-style:normal;color:#888}
.footer p{position:absolute;left:90px;top:39px}
.top{position:absolute;left:704px;top:13px;width:26px;height:26px;border-radius:50%;background:#777;display:flex;align-items:center;justify-content:center}
</style>
</head>
<body>

<header>
  <div class="brand">Fenwick Marlow<small>PTY LTD</small></div>
  <div class="social" aria-label="Social links"><span></span><span></span><span></span><span></span><span></span></div>
  <div class="search">Search
    <svg width="10" height="10" viewBox="0 0 10 10"><circle cx="4" cy="4" r="3" fill="none" stroke="#999" stroke-width="1.2"/><line x1="6.3" y1="6.3" x2="9" y2="9" stroke="#999" stroke-width="1.3"/></svg>
  </div>
  <nav class="nav">
    <a class="active">Home</a><a>Leadership</a><a>Team Coaching</a><a>Individual Development</a><a>About Us</a><a>Contact</a>
  </nav>
</header>
<div class="rule"></div>

<section class="hero" role="img" aria-label="Photo of a team meeting in an office">
  <div class="arrow"><svg width="17" height="22"><polyline points="6,6 11,11 6,16" fill="none" stroke="#fff" stroke-width="1"/></svg></div>
  <div class="caption">
    <h2>Duis accumsan laoreet neque eget venenatis</h2>
    <p>Curabitur bibendum neque non nisl venenatis, sed dictum nulla venenatis. Nullam eget tempus dolor.</p>
    <a class="btn-light">Learn More</a>
  </div>
</section>

<main class="posts">
  <article class="post"><div class="pic" role="img" aria-label="Photo of colleagues working around a table" style="background:linear-gradient(135deg,#6b5a4c,#c9b8a6 60%,#4a4a55)"></div>
    <h3>Curabitur bibendum neque non nisl venenatis, sed dictum nulla venenatis.</h3><time>10 October, 2016</time>
    <p>Nam libero massa, aliquet eget egestas a, convallis eget velit. Etiam blandit ut lectus id congue. Proin justo sapien, mattis id sapien quis, auctor laoreet nibh. Suspendisse dictum.</p></article>
  <article class="post"><div class="pic" role="img" aria-label="Photo of a chess piece on a pale blue board" style="background:linear-gradient(180deg,#e8f0f8,#a9c8e6)"></div>
    <h3>Curabitur bibendum neque non nisl venenatis, sed dictum nulla venenatis.</h3><time>10 October, 2016</time>
    <p>Nam libero massa, aliquet eget egestas a, convallis eget velit. Etiam blandit ut lectus id congue. Proin justo sapien, mattis id sapien quis, auctor laoreet nibh. Suspendisse dictum.</p></article>
  <article class="post"><div class="pic" role="img" aria-label="Photo of a businessman overlooking a city" style="background:linear-gradient(135deg,#e6cdb2,#b99b82 60%,#8b7b72)"></div>
    <h3>Curabitur bibendum neque non nisl venenatis, sed dictum nulla venenatis.</h3><time>10 October, 2016</time>
    <p>Nam libero massa, aliquet eget egestas a, convallis eget velit. Etiam blandit ut lectus id congue. Proin justo sapien, mattis id sapien quis, auctor laoreet nibh. Suspendisse dictum.</p></article>
  <article class="post"><div class="pic" role="img" aria-label="Photo of hands arranging sticky notes on a desk" style="background:linear-gradient(135deg,#3a4a5a,#c7c2c0 55%,#e7d3c9)"></div>
    <h3>Curabitur bibendum neque non nisl venenatis, sed dictum nulla venenatis.</h3><time>10 October, 2016</time>
    <p>Nam libero massa, aliquet eget egestas a, convallis eget velit. Etiam blandit ut lectus id congue. Proin justo sapien, mattis id sapien quis, auctor laoreet nibh. Suspendisse dictum.</p></article>
  <article class="post"><div class="pic" role="img" aria-label="Illustration of business people flying forward with arrows" style="background:linear-gradient(135deg,#4d7fbf,#8fb4dc 60%,#d9e6f2)"></div>
    <h3>Curabitur bibendum neque non nisl venenatis, sed dictum nulla venenatis.</h3><time>10 October, 2016</time>
    <p>Nam libero massa, aliquet eget egestas a, convallis eget velit. Etiam blandit ut lectus id congue. Proin justo sapien, mattis id sapien quis, auctor laoreet nibh. Suspendisse dictum.</p></article>
  <article class="post"><div class="pic" role="img" aria-label="Photo of one green match among red matches" style="background:linear-gradient(180deg,#1d4b4f,#3c6b6a 50%,#c8344f)"></div>
    <h3>Curabitur bibendum neque non nisl venenatis, sed dictum nulla venenatis.</h3><time>10 October, 2016</time>
    <p>Nam libero massa, aliquet eget egestas a, convallis eget velit. Etiam blandit ut lectus id congue. Proin justo sapien, mattis id sapien quis, auctor laoreet nibh. Suspendisse dictum.</p></article>
</main>

<div class="pager"><span>«</span><span>1</span><span>2</span><span>3</span><span>4</span><span>5</span><span>»</span></div>

<aside class="side latest" style="top:112px">
  <h4>LATEST POSTS</h4>
  <div class="list">
    <div class="item"><div class="thumb" role="img" aria-label="Photo of a group of business people" style="background:linear-gradient(#eee,#556)"></div><div><a>Donec feugiat malesuada tortor, at sagittis massa rhoncus ac</a><div class="more">Learn More</div></div></div>
    <div class="item" style="padding-top:8px;height:67px"><div class="thumb" role="img" aria-label="Photo of red business figures" style="background:linear-gradient(135deg,#7a1a1a,#d33)"></div><div><a>Donec feugiat malesuada tortor, at sagittis massa rhoncus ac</a><div class="more">Learn More</div></div></div>
    <div class="item" style="padding-top:8px"><div class="thumb" role="img" aria-label="Photo of a standout yellow figure in a row" style="background:linear-gradient(90deg,#222,#b8a060,#333)"></div><div><a>Donec feugiat malesuada tortor, at sagittis massa rhoncus ac</a><div class="more">Learn More</div></div></div>
    <div class="item" style="padding-top:8px"><div class="thumb" role="img" aria-label="Photo of a presenter in an office" style="background:linear-gradient(135deg,#ddd,#3a5fa0)"></div><div><a>Donec feugiat malesuada tortor, at sagittis massa rhoncus ac</a><div class="more">Learn More</div></div></div>
  </div>
  <a class="view-all">VIEW ALL</a>
</aside>

<div class="promo" role="img" aria-label="Photo of a person with a flag on a mountain summit">
  <h5>Duis accumsan<br>laoreet ante</h5>
  <a class="btn-light">Learn More</a>
</div>

<aside class="side popular" style="top:623px">
  <h4>POPULAR POSTS</h4>
  <div class="list">
    <div class="item"><div class="thumb" role="img" aria-label="Photo of a meeting room" style="background:linear-gradient(135deg,#eee,#6a7a90)"></div><div><a>Donec feugiat malesuada tortor, at sagittis massa rhoncus ac</a><div class="more">Learn More</div></div></div>
    <div class="item" style="padding-top:8px"><div class="thumb" role="img" aria-label="Photo of a figure climbing stairs" style="background:linear-gradient(#f2f2f2,#777)"></div><div><a>Donec feugiat malesuada tortor, at sagittis massa rhoncus ac</a><div class="more">Learn More</div></div></div>
    <div class="item" style="padding-top:8px"><div class="thumb" role="img" aria-label="Chalkboard drawing with arrows" style="background:linear-gradient(135deg,#333,#555)"></div><div><a>Donec feugiat malesuada tortor, at sagittis massa rhoncus ac</a><div class="more">Learn More</div></div></div>
    <div class="item" style="padding-top:8px"><div class="thumb" role="img" aria-label="Photo of a person on a cliff at sunset" style="background:linear-gradient(#e8d6c0,#6b5f5a)"></div><div><a>Donec feugiat malesuada tortor, at sagittis massa rhoncus ac</a><div class="more">Learn More</div></div></div>
  </div>
  <a class="view-all">VIEW ALL</a>
</aside>

<aside class="side signup" style="top:955px">
  <h4>NEWSLETTER SIGNUP</h4>
  <form>
    <div class="field">Email Address</div>
    <div class="send"><svg width="10" height="8" viewBox="0 0 10 8"><rect x="0.5" y="0.5" width="9" height="7" fill="#fff"/><polyline points="0.5,0.5 5,4.5 9.5,0.5" fill="none" stroke="#c588bc" stroke-width="1"/></svg></div>
  </form>
</aside>

<footer class="footer">
  <nav><a>Home</a><i>|</i><a>Leadership</a><i>|</i><a>Team Coaching</a><i>|</i><a>Individual Development</a><i>|</i><a>About Us</a><i>|</i><a>Contact</a></nav>
  <p>Copyright © 2016 Fenwick Marlow Pty. All rights reserved.</p>
  <div class="top"><svg width="12" height="9"><polygon points="6,0 12,9 0,9" fill="#2b2b2b"/></svg></div>
</footer>

</body>
</html>
```